Client website

Our designer we were working with had some personal things come up and was unable to finish the design for the site.

We have a .psd file started, and will be attaching it to the project.

Reason: I still want to polish the designs with the current designer and allow more designers the opportunity to participate.

Reason: I'm extending the deadline for another day to give everyone enough time for the final changes our client wants.

I'm trying to extend the deadline so we can get one last set of comps in for my client.  Could everyone message me and let me know how much time they need to do the final tweaks?

Reason: Hey everyone.  I've been sick the last 3 days and I haven't been able to provide feedback on designs.  I'm extending just a few more days so I can catch up here.  Thanks everyone for your patience.

Adults in United States aged 25 to 60 that handle the household budgets and maintenance.

• 1) We need 2 pages. 1 page for flood restoration, 1 page for carpet cleaning

2) The 1-800-# must be the focal point of the website for both pages. People are mostly looking to contact someone ASAP to get them out to their house when flooding occurs.

3) We''re going to have a slide show area to high-light different sub-services offered for each page.

4) We really want a pagenest / lumora feed area. We''re going to use pagenest for special offers, and lumora for weather updates. The pagenest feed is going to be on the carpet cleaning page. The lumora feed is going to be on the flood page.

5) We want an SEO text sections near the bottom.

6) The very bottom will link to the privacy policy and user agreement as well as company name and copyright details.

We really want to stick to the say "theme" that our first designer started with.
• I'm not a designer, so if you think something looks better somewhere, or something can be eliminated, or something can be enhanced, but all means, let us know.

```html
<!DOCTYPE html>
<html lang="en">
<head>
<meta charset="utf-8">
<title>Pure-Weave Carpet Cleaning</title>
<link rel="stylesheet" href="https://fonts.googleapis.com/css2?family=PT+Sans:wght@400;700&family=Gochi+Hand&display=swap">
<style>
:root{
  --bg-top:#2e3a44;
  --bg-bottom:#050505;
  --frame-blue:#1a74c4;
  --frame-dark:#0d4f94;
  --carpet:#8d8780;
  --carpet-dark:#6e6961;
  --panel:#ebe8e4;
  --panel-edge:#f6f4f1;
  --title-blue:#1f7cc4;
  --body-gray:#6b6b6b;
  --nav-green:#2fae3a;
  --nav-blue:#2a8fd6;
  --btn-green:#29a833;
  --note:#eeeadc;
  --footer-text:#4f4f4f;
  --white:#ffffff;
}
*{margin:0;padding:0;box-sizing:border-box}
html,body{width:1200px;height:1200px;overflow:hidden}
body{
  position:relative;
  background:linear-gradient(180deg,var(--bg-top) 0%,#1c242b 45%,var(--bg-bottom) 85%);
  font-family:Arial,Helvetica,sans-serif;
}
.site-frame{
  position:absolute;left:134px;top:0;width:935px;height:940px;
  background:var(--frame-blue);
  border-bottom:4px solid var(--frame-dark);
  box-shadow:0 0 40px rgba(0,0,0,.6);
}
.site-inner{
  position:absolute;left:6px;top:0;width:925px;height:935px;
  background:radial-gradient(ellipse at 50% 30%,var(--carpet) 0%,var(--carpet-dark) 100%);
}
.hero-photo{
  position:absolute;left:0;top:0;width:925px;height:315px;
  background:linear-gradient(180deg,#9a9893 0%,#b3b0aa 60%,#8f8b85 100%);
}
.brand{
  position:absolute;left:48px;top:70px;width:250px;text-align:center;
}
.brand-mark{
  width:110px;height:110px;border-radius:50%;margin:0 auto 14px;
  background:var(--title-blue);
}
.brand-name{
  font-family:"PT Sans",sans-serif;font-weight:700;font-size:36px;
  color:var(--nav-green);letter-spacing:1px;line-height:1;
}
.brand-tag{
  font-family:"PT Sans",sans-serif;font-size:13px;color:#333;letter-spacing:1px;margin-top:4px;
}
.main-nav{
  position:absolute;left:0;top:315px;width:800px;height:35px;display:flex;
  background:var(--nav-blue);
}
.main-nav a{
  width:147px;height:35px;display:block;text-align:center;
  font-family:"PT Sans",sans-serif;font-size:17px;letter-spacing:1.5px;color:var(--white);
  text-decoration:none;line-height:38px;border-right:1px solid #1b6db0;
  background:linear-gradient(180deg,#48a6e6,var(--nav-blue));
}
.main-nav a.is-current{background:linear-gradient(180deg,#47c74f,var(--nav-green))}
.call-note{
  position:absolute;left:905px;top:175px;width:230px;height:210px;
  background:var(--note);transform:rotate(22deg);
  box-shadow:4px 6px 12px rgba(0,0,0,.4);
  font-family:"Gochi Hand",cursive;color:#333;text-align:center;padding-top:52px;
}
.call-note .lead{font-size:34px}
.call-note .phone{font-size:26px;margin-top:6px}
.call-pin{position:absolute;left:950px;top:155px;width:22px;height:22px;border-radius:50%;background:var(--nav-green)}
.slide-panel{
  position:absolute;left:178px;top:395px;width:844px;height:297px;border-radius:18px;
  background:var(--panel);box-shadow:0 2px 6px rgba(0,0,0,.25);
}
.slide-title{
  position:absolute;left:44px;top:38px;
  font-family:"PT Sans",sans-serif;font-weight:700;font-size:50px;letter-spacing:-2px;color:var(--title-blue);
}
.slide-copy{
  position:absolute;left:48px;top:130px;width:510px;
  font-size:16px;line-height:18px;color:var(--body-gray);
}
.slide-copy p+p{margin-top:18px}
.cta-button{
  position:absolute;left:613px;top:171px;width:177px;height:44px;border-radius:7px;
  background:linear-gradient(180deg,#4fd05a,var(--btn-green));
  font-family:"PT Sans",sans-serif;font-weight:700;font-size:23px;color:var(--white);
  text-align:center;line-height:44px;letter-spacing:-.5px;box-shadow:0 3px 4px rgba(0,0,0,.3);
}
.slide-arrow{position:absolute;top:522px;width:45px;height:45px}
.slide-arrow.prev{left:155px}
.slide-arrow.next{left:999px}
.feed-card{
  position:absolute;width:400px;height:172px;border-radius:10px;background:var(--panel);
  box-shadow:0 2px 6px rgba(0,0,0,.25);
}
.feed-card.pagenest{left:178px;top:733px}
.feed-card.lumora{left:621px;top:736px}
.feed-icon{position:absolute;left:43px;top:38px;width:64px;height:64px;border-radius:6px;background:#5a7bbf}
.feed-card.lumora .feed-icon{left:35px;top:41px;background:#d8e6ef}
.follow-btn{
  position:absolute;left:35px;top:113px;width:81px;height:21px;background:var(--panel-edge);
  border:1px solid #bbb;font-size:11px;text-align:center;line-height:20px;color:#222;
}
.feed-card.lumora .follow-btn{left:26px;top:113px}
.feed-title{
  position:absolute;left:142px;top:28px;
  font-family:"PT Sans",sans-serif;font-weight:700;font-size:31px;letter-spacing:-1px;color:var(--title-blue);
}
.feed-text{
  position:absolute;left:142px;top:70px;width:245px;font-size:13px;line-height:15px;color:var(--body-gray);
}
.feed-card.lumora .feed-title,.feed-card.lumora .feed-text{left:135px}
.seo-text{
  position:absolute;left:179px;top:961px;width:845px;font-size:11px;line-height:15px;color:var(--footer-text);
}
.site-footer{
  position:absolute;left:179px;top:1082px;width:846px;display:flex;justify-content:space-between;
  font-size:11px;color:var(--white);
}
.site-footer a{color:var(--white);text-decoration:none}
</style>
</head>
<body>
<div class="site-frame">
  <div class="site-inner">
    <div class="hero-photo" role="img" aria-label="Photo of a modern room with a lounge chair and a vacuum cleaner on fresh carpet"></div>
    <div class="brand">
      <div class="brand-mark"></div>
      <div class="brand-name">PURE-WEAVE</div>
      <div class="brand-tag">Carpet Cleaning</div>
    </div>
    <nav class="main-nav">
      <a class="is-current" href="#">home</a>
      <a href="#">about</a>
      <a href="#">services</a>
      <a href="#">faq</a>
      <a href="#">contact</a>
    </nav>
  </div>
</div>

<div class="call-note">
  <div class="lead">Call Us Now!</div>
  <div class="phone">1-800-555-0142</div>
</div>
<div class="call-pin"></div>

<section class="slide-panel">
  <h1 class="slide-title">Sub-service Number One</h1>
  <div class="slide-copy">
    <p>Lorem ipsum dolor sit amet, consectetur adipiscing elit. Duis semper, turpis in sodales ultricies, felis dui facilisis sem, nec dignissim augue nisl eu eros. Sed a faucibus massa.</p>
    <p>Suspendisse id felis tellus, vel sagittis sem. Fusce aliquam scelerisque diam et tempor.</p>
  </div>
  <div class="cta-button">A Button »</div>
</section>

<svg class="slide-arrow prev" viewBox="0 0 45 45" aria-label="Previous slide">
  <circle cx="22.5" cy="22.5" r="21" fill="#1f8ad8" stroke="#fff" stroke-width="2"/>
  <path d="M21 15 L14 22.5 L21 30 M30 15 L23 22.5 L30 30" fill="none" stroke="#fff" stroke-width="3.5"/>
</svg>
<svg class="slide-arrow next" viewBox="0 0 45 45" aria-label="Next slide">
  <circle cx="22.5" cy="22.5" r="21" fill="#1f8ad8" stroke="#fff" stroke-width="2"/>
  <path d="M15 15 L22 22.5 L15 30 M24 15 L31 22.5 L24 30" fill="none" stroke="#fff" stroke-width="3.5"/>
</svg>

<section class="feed-card pagenest">
  <div class="feed-icon"></div>
  <div class="follow-btn">Follow us!</div>
  <h2 class="feed-title">pagenest Feed</h2>
  <p class="feed-text">- Lorem ipsum dolor sit amet, consectetur adipiscing elit. Duis semper, turpis in sodales ultricies, felis dui facilisis sem, nec dignissim</p>
</section>

<section class="feed-card lumora">
  <div class="feed-icon"></div>
  <div class="follow-btn">Follow us!</div>
  <h2 class="feed-title">lumora Feed</h2>
  <p class="feed-text">- Lorem ipsum dolor sit amet, consectetur adipiscing elit. Duis semper, turpis in sodales ultricies, felis dui facilisis sem, nec dignissim</p>
</section>

<p class="seo-text">Lorem ipsum dolor sit amet, consectetur adipiscing elit. Etiam mattis dolor placerat sem iaculis dapibus. Praesent velit nibh, sollicitudin vel feugiat sit amet, bibendum id urna. Etiam eleifend tellus a turpis rutrum mollis et non massa. Vivamus eu porta felis. Etiam sodales enim magna, eu imperdiet nulla. Duis tincidunt enim ut massa faucibus ullamcorper. Donec ac sem odio, ut convallis risus. Suspendisse gravida vestibulum bibendum. Aenean aliquet dui quis justo sollicitudin sit amet euismod libero facilisis. Donec consectetur elit luctus lacus consequat ut porttitor risus varius. Pellentesque interdum, sem sed commodo ornare, sem est semper turpis, a viverra sem enim a erat. Cras sollicitudin leo id magna condimentum faucibus. Class aptent taciti sociosqu ad litora torquent per conubia nostra, per inceptos himenaeos. In vulputate, eros non sodales placerat, dolor lectus sollicitudin augue, elementum semper elit leo vel nulla. Aenean faucibus cursus magna in ornare. Nunc porta, purus porta egestas ornare, nunc nisl molestie sem, id aliquam nisi justo quis massa. In id placerat nibh. Aliquam risus mi, rhoncus et lacinia ac, pharetra convallis ipsum. Phasellus volutpat turpis vitae</p>

<footer class="site-footer">
  <span>Copyright 2010. Pure-Weave.</span>
  <span><a href="#">Privacy Policy</a> | <a href="#">User Agreement</a></span>
</footer>
</body>
</html>
```